Design business card for new business which advocates for elders in nursing homes or personal care h

New business for rights of the elderly residents who reside in personal care homes and or nursing homes. I am looking for a business card with logo of keystone for Pennsylvania and something in side the keystone that represents healthcare, advocates, something on that line; monitor care received and needs of resident. Chart audits, State Regulation compliance

Target Market(s)

Seniors no longer safe to live at home by themselves along with their kids

Industry/Entity Type

Business

Contact Information for Business Card

Keystone symbol to represent Pensylvaoa with some kind of symbol inside to represent advocate, seniors, or healthcare symbol

Font styles to use
Serif

Colors
33a6d7
85cae6
abd037

Requirements
Must have
• Brightwell Elder Allies is our business name; our tag line is Path to Better Living
Nice to have
• Nice logo

```html
<!DOCTYPE html>
<html lang="en">
<head>
<meta charset="utf-8">
<title>Brightwell Elder Allies – Business Card</title>
<link rel="stylesheet" href="https://fonts.googleapis.com/css2?family=Libre+Baskerville:wght@400;700&display=swap">
<style>
  :root {
    --brand-blue: #33a6d7;
    --brand-sky: #85cae6;
    --brand-green: #abd037;
    --paper: #ffffff;
    --backdrop: #ece9e4;
    --ink-white: #ffffff;
  }
  * { box-sizing: border-box; margin: 0; padding: 0; }
  html, body {
    width: 1200px; height: 1000px; overflow: hidden;
    background: var(--backdrop);
    font-family: "Libre Baskerville", Georgia, serif;
  }
  .canvas {
    width: 1200px; height: 1000px;
    display: flex; flex-direction: column; align-items: center; justify-content: center;
    gap: 44px;
  }
  .card {
    width: 860px; height: 430px;
    background: var(--paper);
    box-shadow: 0 6px 18px rgba(0,0,0,0.18);
    display: flex;
    overflow: hidden;
  }
  .brand-block {
    flex: 1;
    display: flex; flex-direction: column; align-items: center; justify-content: center;
    gap: 18px;
  }
  .brand-badge {
    width: 150px; height: 150px; border-radius: 50%;
    background: var(--brand-blue);
  }
  .brand-name {
    color: var(--brand-blue);
    font-weight: 700;
    text-transform: uppercase;
    text-align: center;
    line-height: 1;
  }
  .brand-name .line-main { display: block; font-size: 40px; letter-spacing: 1px; }
  .brand-name .line-sub { display: block; font-size: 21px; letter-spacing: 1.5px; margin-top: 4px; }
  .brand-tagline {
    color: var(--brand-green);
    font-size: 14px; letter-spacing: 2px; text-transform: uppercase;
  }
  .card--back .brand-block { flex: 0 0 50%; }
  .contact-panel {
    flex: 0 0 50%;
    background: var(--brand-blue);
    display: flex; flex-direction: column; justify-content: center; align-items: flex-end;
    padding-right: 40px;
    gap: 16px;
  }
  .contact-row {
    display: flex; align-items: center; gap: 14px;
    color: var(--ink-white);
    font-size: 19px;
  }
  .contact-icon {
    width: 30px; height: 30px; border-radius: 50%;
    background: var(--brand-green);
    display: flex; align-items: center; justify-content: center;
    flex: none;
  }
  .contact-icon svg { width: 18px; height: 18px; }
  .contact-icon .www { font-family: Arial, sans-serif; font-size: 9px; font-weight: 700; color: var(--ink-white); }
</style>
</head>
<body>
<main class="canvas">
  <section class="card card--front">
    <div class="brand-block">
      <div class="brand-badge"></div>
      <h1 class="brand-name"><span class="line-main">Brightwell</span><span class="line-sub">Elder Allies</span></h1>
      <p class="brand-tagline">Path to Better Living</p>
    </div>
  </section>

  <section class="card card--back">
    <div class="brand-block">
      <div class="brand-badge"></div>
      <h2 class="brand-name"><span class="line-main">Brightwell</span><span class="line-sub">Elder Allies</span></h2>
      <p class="brand-tagline">Path to Better Living</p>
    </div>
    <div class="contact-panel">
      <div class="contact-row"><span>412 730 55816</span>
        <span class="contact-icon"><svg viewBox="0 0 24 24"><path fill="#fff" d="M6.6 10.8a15 15 0 0 0 6.6 6.6l2.2-2.2a1 1 0 0 1 1-.25 11.4 11.4 0 0 0 3.6.57 1 1 0 0 1 1 1V20a1 1 0 0 1-1 1A17 17 0 0 1 3 4a1 1 0 0 1 1-1h3.5a1 1 0 0 1 1 1c0 1.25.2 2.45.57 3.57a1 1 0 0 1-.25 1z"/></svg></span>
      </div>
      <div class="contact-row"><span>po box, city, state, zip</span>
        <span class="contact-icon"><svg viewBox="0 0 24 24"><path fill="#fff" d="M12 2a7 7 0 0 0-7 7c0 5.2 7 13 7 13s7-7.8 7-13a7 7 0 0 0-7-7zm0 9.5A2.5 2.5 0 1 1 12 6.5a2.5 2.5 0 0 1 0 5z"/></svg></span>
      </div>
      <div class="contact-row"><span>hello@brightwellallies.com</span>
        <span class="contact-icon"><svg viewBox="0 0 24 24"><rect x="3" y="6" width="18" height="12" rx="1" fill="#fff"/><path d="M3.5 6.5 12 13l8.5-6.5" fill="none" stroke="#abd037" stroke-width="1.6"/></svg></span>
      </div>
      <div class="contact-row"><span>brightwellallies.com</span>
        <span class="contact-icon"><span class="www">www</span></span>
      </div>
    </div>
  </section>
</main>
</body>
</html>
```